Mirela Causo Photography

I need a website design for my photography business, I want something clean, elegant, Classy.. I like the colors, White, Black, Green/Blue, Pink, Brown, Lavender,, I have a lot added my Logo .... Additional Info... I need a Photography Website Design, with probably 6 Tabs, Home, About Me, Portfolio, Gallery, Investment, Contact.
Home Page should have my logo, Name & Address, Social Media Icons, and Pictures.
As long as the templates are made I have a hosting coming that will code it.
Target Market(s)
Portraits Photography, Senior Portraits, Newborn, Families, Events, Engagements, Wedding,
Industry/Entity Type
Business
Number of Pages Required
5+ page
Look and feel

```html
<!DOCTYPE html>
<html lang="en">
<head>
<meta charset="utf-8">
<title>Mirela Causo Photography</title>
<link rel="stylesheet" href="https://fonts.googleapis.com/css2?family=Josefin+Sans:wght@300&display=swap">
<style>
  :root {
    --page-bg: #0b0b0b;
    --rule: #2e2e2e;
    --text: #f2f2f2;
    --text-soft: #d8d8d8;
    --accent-pink: #d9a3d6;
    --arrow: #bdbdbd;
    --hero-violet: #9b5cd6;
    --hero-pink: #e6a6ee;
    --hero-blue: #4a5fe0;
    --hero-cyan: #7fd6e8;
    --social-one: #4fb3e8;
    --social-two: #d8322a;
    --social-three: #2f7fc8;
  }
  * { margin: 0; padding: 0; box-sizing: border-box; }
  html, body { width: 1200px; height: 674px; overflow: hidden; background: var(--page-bg); }
  body { font-family: "Josefin Sans", sans-serif; font-weight: 300; color: var(--text); position: relative; }

  .header-rule { position: absolute; top: 58px; height: 1px; background: var(--rule); }
  .header-rule--left { left: 94px; width: 326px; }
  .header-rule--right { left: 780px; width: 326px; }

  .brand { position: absolute; left: 450px; top: 22px; width: 300px; text-align: center; color: var(--text); }
  .brand-dot { width: 32px; height: 32px; border-radius: 50%; background: var(--text); margin: 0 auto 4px; }
  .brand-name { font-size: 27px; line-height: 28px; letter-spacing: 0.5px; }
  .brand-sub { font-size: 10px; letter-spacing: 3px; line-height: 12px; text-transform: uppercase; }

  .hero { position: absolute; left: 267px; top: 116px; width: 667px; height: 457px;
    background:
      radial-gradient(ellipse 45% 55% at 45% 60%, var(--hero-pink) 0%, transparent 70%),
      radial-gradient(ellipse 40% 50% at 70% 65%, var(--hero-violet) 0%, transparent 75%),
      linear-gradient(115deg, var(--hero-blue) 0%, var(--hero-violet) 45%, var(--hero-cyan) 100%); }

  .slider-arrow { position: absolute; top: 308px; width: 28px; height: 58px; }
  .slider-arrow--prev { left: 179px; }
  .slider-arrow--next { left: 993px; }

  .main-nav { position: absolute; top: 592px; left: 0; width: 1200px; display: flex; justify-content: center; gap: 21px; padding-left: 2px; }
  .main-nav a { color: var(--text-soft); text-decoration: none; font-size: 14.5px; letter-spacing: 0.2px; text-transform: uppercase; padding-bottom: 6px; }
  .main-nav a.is-active { color: var(--accent-pink); border-bottom: 1px solid var(--accent-pink); }

  .footer-rule { position: absolute; top: 641px; left: 94px; width: 1012px; height: 1px; background: var(--rule); }
  .follow { position: absolute; top: 651px; left: 96px; display: flex; align-items: center; gap: 7px; font-size: 12px; color: var(--text-soft); }
  .follow-label { margin-right: 4px; }
  .social-square { width: 14px; height: 14px; display: block; }
  .social-square--one { background: var(--social-one); }
  .social-square--two { background: var(--social-two); }
  .social-square--three { background: var(--social-three); }
  .legal { position: absolute; top: 652px; right: 96px; font-size: 12px; color: var(--text-soft); white-space: nowrap; }
</style>
</head>
<body>
  <div class="header-rule header-rule--left"></div>
  <div class="header-rule header-rule--right"></div>

  <header class="brand">
    <div class="brand-dot"></div>
    <div class="brand-name">mirela causo</div>
    <div class="brand-sub">photography</div>
  </header>

  <svg class="slider-arrow slider-arrow--prev" viewBox="0 0 28 58" aria-label="Previous slide">
    <polyline points="26,1 2,29 26,57" fill="none" stroke="var(--arrow)" stroke-width="1.2"/>
  </svg>

  <div class="hero" role="img" aria-label="Fashion portrait of a model in a sculpted pink and lavender ruffled gown in a blue-lit room"></div>

  <svg class="slider-arrow slider-arrow--next" viewBox="0 0 28 58" aria-label="Next slide">
    <polyline points="2,1 26,29 2,57" fill="none" stroke="var(--text)" stroke-width="1.2"/>
  </svg>

  <nav class="main-nav">
    <a href="#" class="is-active">Home</a>
    <a href="#">About Me</a>
    <a href="#">Portfolio</a>
    <a href="#">Gallery</a>
    <a href="#">Investment</a>
    <a href="#">Contact Us</a>
  </nav>

  <div class="footer-rule"></div>
  <div class="follow">
    <span class="follow-label">Follow Us</span>
    <span class="social-square social-square--one"></span>
    <span class="social-square social-square--two"></span>
    <span class="social-square social-square--three"></span>
  </div>
  <div class="legal">Terms &amp; Conditions &nbsp;| &nbsp;Privacy Policy &nbsp;| All Rights Reserved Mirela Causo Photography 2015.</div>
</body>
</html>
```